Basisdesign Buch-/E-Book-Cover für Haldmoor-Krimis
Zielgruppe
Ich schreibe Krimis, Thriller, Kriminalstories, Krimiparodien.
Meine Zielgruppe sind deutschsprachige Krimi-Leser.
Aufgabenstellung
Ich benötige ein Basisdesign für Buchcover (Höhe 2.343, Breite 1.518 Pixel – Druckfalter, eBooks). Alle Bücher haben mit Crime zu tun, aber in verschiedenen Unter-Genres: Klassischer Kriminalroman, Thriller, Fantasy Thriller, Kurzgeschichten, Krimi-Parodien.
Ich benötige, quasi als Marke, dafür ein gleichbleibendes grafisches Element, z. B. einen Sockel im unteren Coverbereich, der den Autorennamen „Jonas Haldmoor“ und das jeweilige Unter-Genre enthält. Unter-Genres sind: Krimi, Thriller, Fantasy-Thriller, Kurzgeschichten und Krimi-Parodie. Das alles sollte auch noch im Format der Lesoria-Bücherlisten wie „Kunden kauften auch“ halbwegs lesbar sein.
Ein bisschen mörderisch und blutig sind alle Varianten.
Nachdem die Bandbreite vom Thriller bis zur Parodie reicht, sollte der gleichbleibende Markenbereich eine entsprechende grafische Bandbreite aufweisen, dabei aber die Grundmelodie Crime nicht aus den Augen verlieren.
Im oberen Bereich stelle ich mir Grafiken oder Hintergrundfotos vor, die für jedes Buch individuell gestaltet werden müssten, was jedoch über das Basisdesign hinausgeht. Die Wahl der Schriftart für Titel (bislang 11 – 25 Zeichen inkl. Leerzeichen) und allfällige Untertitel (im Umfang von maximal 30 Zeichen), sollte zu denen im Sockel passen.

```html
<!DOCTYPE html>
<html lang="de">
<head>
<meta charset="utf-8">
<title>Serena Moretti – Die Spiegelfalle</title>
<link href="https://fonts.googleapis.com/css2?family=Oswald:wght@500&family=Playfair+Display:ital,wght@0,400;1,400&display=swap" rel="stylesheet">
<style>
  :root {
    --night: #0d2a6b;
    --deep-blue: #1b4aa0;
    --sky: #5c93cf;
    --cloud: #dfe9f1;
    --city-warm: #c89a52;
    --river: #3f8fa0;
    --title-cyan: #2bd3ff;
    --band-cyan: #12b9e8;
    --paper: #ffffff;
    --ink: #111a22;
  }
  html, body {
    margin: 0;
    padding: 0;
    overflow: hidden;
    background: #ffffff;
  }
  .cover {
    position: relative;
    width: 768px;
    height: 1200px;
    overflow: hidden;
  }
  .cover svg {
    display: block;
  }
  .title-text {
    font-family: "Oswald", "Arial Narrow", sans-serif;
    font-weight: 500;
    fill: var(--title-cyan);
  }
  .genre {
    font-family: "Playfair Display", Georgia, serif;
    font-style: italic;
    fill: var(--ink);
  }
  .author {
    font-family: "Playfair Display", Georgia, serif;
    fill: var(--paper);
  }
</style>
</head>
<body>
<div class="cover">
  <svg width="768" height="1200" viewBox="0 0 768 1200" xmlns="http://www.w3.org/2000/svg">
    <defs>
      <linearGradient id="scene-gradient" x1="0" y1="0" x2="0" y2="1">
        <stop offset="0" stop-color="var(--night)"/>
        <stop offset="0.35" stop-color="var(--deep-blue)"/>
        <stop offset="0.55" stop-color="var(--sky)"/>
        <stop offset="0.66" stop-color="var(--cloud)"/>
        <stop offset="0.76" stop-color="var(--city-warm)"/>
        <stop offset="0.88" stop-color="var(--city-warm)"/>
        <stop offset="1" stop-color="var(--river)"/>
      </linearGradient>
      <linearGradient id="water-gradient" x1="0" y1="0" x2="0" y2="1">
        <stop offset="0" stop-color="#4a9fc0"/>
        <stop offset="1" stop-color="#1f6d98"/>
      </linearGradient>
    </defs>

    <rect class="scene-photo" x="0" y="0" width="768" height="860" fill="url(#scene-gradient)"
          role="img" aria-label="Foto: Himmel mit Wolken über einer Flusslandschaft mit historischer Brücke und Häusern, mit Blutspritzern"/>
    <rect class="water-photo" x="0" y="1090" width="768" height="110" fill="url(#water-gradient)"
          role="img" aria-label="Foto: Wasseroberfläche des Flusses"/>

    <g class="book-title">
      <text class="title-text" x="123" y="246" font-size="190" textLength="522" lengthAdjust="spacingAndGlyphs">SERENA</text>
      <text class="title-text" x="65" y="457" font-size="186" textLength="638" lengthAdjust="spacingAndGlyphs">MORETTI</text>
      <text class="title-text" x="173" y="541" font-size="58" textLength="422" lengthAdjust="spacingAndGlyphs">DIE SPIEGELFALLE</text>
    </g>

    <g class="plinth">
      <path class="torn-edge-top" fill="var(--paper)"
            d="M0 836 L30 828 L58 833 L92 820 L120 826 L160 818 L200 829 L240 822 L280 831 L318 824 L360 833 L400 826 L440 832 L480 825 L520 830 L560 823 L600 829 L640 821 L680 830 L720 824 L768 828 L768 860 L0 860 Z"/>
      <path class="band" fill="var(--band-cyan)"
            d="M0 845 L40 840 L80 846 L130 838 L180 845 L230 839 L290 846 L350 840 L410 847 L470 841 L530 846 L590 839 L650 845 L710 840 L768 844 L768 1100 L0 1100 Z"/>
      <path class="torn-edge-bottom" fill="var(--paper)"
            d="M0 1098 L40 1092 L80 1100 L120 1094 L170 1101 L220 1095 L270 1100 L320 1093 L370 1099 L420 1092 L470 1100 L520 1094 L570 1101 L620 1093 L670 1100 L720 1095 L768 1099 L768 1112 L720 1116 L670 1110 L620 1117 L570 1111 L520 1118 L470 1112 L420 1117 L370 1110 L320 1116 L270 1111 L220 1117 L170 1112 L120 1118 L80 1111 L40 1116 L0 1112 Z"/>

      <text class="genre" x="230" y="933" font-size="34" textLength="308" lengthAdjust="spacingAndGlyphs">Fantasy-Thriller</text>

      <rect class="quill-mark" x="590" y="884" width="96" height="96" rx="48" fill="#0e5e78" opacity="0.55"
            role="img" aria-label="Illustration: schwarze Schreibfeder"/>

      <text class="author" x="92" y="1052" font-size="100" textLength="584" lengthAdjust="spacingAndGlyphs">Jonas Haldmoor</text>
    </g>
  </svg>
</div>
</body>
</html>
```